New Web Design Project

website name will be called www.brightmarasun.com
Please us color red, white,grey if possible
We are a solar provider that will offer solar ownership and leases with 25yr warranty and labor. Over 20yrs combined solar experience

Number of Pages Required

1 page

```html
<!DOCTYPE html>
<html lang="en">
<head>
<meta charset="utf-8">
<title>Brightmara Sun – Solar Ownership &amp; Leases</title>
<link href="https://fonts.googleapis.com/css2?family=Michroma&family=Roboto:ital,wght@0,400;0,500;0,700;1,400&display=swap" rel="stylesheet">
<style>
:root{
  --red:#d10a0a;
  --red-dark:#a80000;
  --grey:#6f6f6f;
  --grey-dark:#4a4a4a;
  --grey-light:#ececec;
  --text:#777;
  --white:#fff;
  --heading:#666;
}
*{margin:0;padding:0;box-sizing:border-box}
html,body{width:1200px;height:4601px;overflow:hidden}
body{position:relative;background:var(--white);font-family:'Roboto',sans-serif;color:var(--text)}
section,header,footer{position:absolute;left:0;width:1200px}
.brand{font-family:'Roboto',sans-serif;font-weight:700;color:var(--grey);letter-spacing:1px;display:flex;align-items:center;gap:10px}
.brand .dot{width:14px;height:14px;border-radius:50%;background:var(--red)}
.title{font-family:'Michroma',sans-serif;font-size:42px;color:var(--heading);text-align:center;letter-spacing:2px}
.title b{color:var(--red);font-weight:400}
.btn{display:inline-flex;align-items:center;justify-content:center;gap:8px;background:var(--red);color:var(--white);font-weight:700;border-radius:30px;font-size:15px}
.btn svg{width:14px;height:14px}

/* header */
.site-header{top:0;height:116px;background:var(--white)}
.site-header .brand{position:absolute;left:110px;top:36px;font-size:34px}
.social-top{position:absolute;left:523px;top:23px;display:flex;gap:8px}
.social-top span{width:30px;height:30px;border:1.5px solid #666;border-radius:50%}
.call{position:absolute;left:705px;top:18px;display:flex;gap:14px;align-items:center}
.call small{display:block;font-size:12px;color:#555}
.call strong{font-size:19px;color:#222}
.quote{position:absolute;left:929px;top:20px;width:157px;height:37px;font-size:14px}
.nav{position:absolute;left:409px;top:83px;display:flex;gap:29px;font-size:15px;font-weight:500;color:#222}
.nav .active{color:var(--red)}

/* hero */
.hero{top:116px;height:670px;background:linear-gradient(180deg,#5e8a4a 0%,#7b8c86 12%,#3c4f69 35%,#2c3a52 60%,#4b5561 85%,#7b8178 100%)}
.hero-copy{position:absolute;top:214px;width:100%;text-align:center;color:var(--white)}
.hero-copy .brand{justify-content:center;color:var(--white);font-size:52px}
.hero-copy .brand .dot{width:18px;height:18px}
.hero-copy p{margin:20px auto 0;width:500px;font-size:17px;line-height:24px;font-weight:500}
.hero-copy .btn{margin-top:24px;width:188px;height:41px;font-size:16px}
.hero-curve{position:absolute;left:0;bottom:0;width:1200px;height:106px}

/* about */
.about{top:786px;height:560px}
.about .title{margin-top:26px}
.about p{width:860px;margin:30px auto 0;text-align:center;font-size:14.5px;line-height:27px;color:#888}
.features{position:absolute;top:241px;left:0;width:1200px;height:240px}
.feature{position:absolute;width:240px;height:240px;top:0;border:2px dashed var(--red);border-radius:50%}
.feature .disc{position:absolute;left:28px;top:28px;width:184px;height:184px;border-radius:50%;background:var(--grey);border:5px solid #fff;box-shadow:0 6px 14px rgba(0,0,0,.25);color:#fff;display:flex;flex-direction:column;align-items:center;justify-content:center;text-align:center;font-weight:500;font-size:15px;line-height:22px;padding:0 14px}
.feature .disc svg{width:44px;height:44px;margin-bottom:10px}
.feature.red .disc{background:var(--red)}
.feature .knot{position:absolute;right:-13px;top:108px;width:24px;height:24px;border-radius:50%;background:var(--red)}

/* services */
.services{top:1346px;height:497px}
.services .title{margin-top:32px}
.service-row{position:absolute;top:119px;left:0;display:flex;width:1200px;height:378px}
.service-row > div{width:300px;height:378px;position:relative}
.photo-house{background:linear-gradient(160deg,#6d9bd1 0%,#3a4f6e 40%,#2b3a52 70%,#56606a 100%)}
.photo-roof{background:linear-gradient(180deg,#4e8fd6 0%,#8aa3b5 30%,#3f4c5e 55%,#9b8d80 80%,#c9b9a8 100%)}
.panel{color:#fff;text-align:center;padding:40px 28px 0}
.panel.grey{background:#7b7b7b}
.panel.red{background:var(--red)}
.panel h3{font-size:21px;font-weight:500;margin-bottom:22px}
.panel p{font-size:13.5px;line-height:26px}
.panel .more{margin-top:20px;display:inline-flex;gap:8px;align-items:center;background:#fff;border-radius:30px;width:166px;height:41px;justify-content:center;font-weight:500;font-size:13px;color:#555}
.panel.red .more{color:var(--red);font-weight:700}
.panel .notch{position:absolute;left:-10px;top:180px;border-right:10px solid;border-top:10px solid transparent;border-bottom:10px solid transparent}
.panel.grey .notch{border-right-color:#7b7b7b}
.panel.red .notch{border-right-color:var(--red)}

/* how it works */
.how{top:1843px;height:532px}
.how .photo{position:absolute;left:111px;top:104px;width:489px;height:325px;background:linear-gradient(150deg,#6fa7d8 0%,#9cc3e3 30%,#5d6c7d 55%,#8b95a3 80%,#cfd8e2 100%)}
.how .copy{position:absolute;left:666px;top:118px;width:440px}
.how .title{text-align:left;font-size:33px;letter-spacing:1px}
.how p{margin-top:28px;font-size:14px;line-height:27.5px;color:#888}
.how .btn{margin-top:26px;width:155px;height:38px;font-size:13px}

/* why choose */
.why{top:2375px;height:572px;background:linear-gradient(180deg,#f6f6f6 0%,#e4e4e4 50%,#d9dadc 100%)}
.why .title{margin-top:68px}
.cards{position:absolute;top:172px;left:111px;display:flex;gap:20px}
.card{width:312px;height:296px;background:#fff;border-radius:60px 0 60px 0;text-align:center;padding-top:30px;box-shadow:0 4px 12px rgba(0,0,0,.06)}
.card .icon{width:94px;height:94px;border-radius:50%;background:var(--grey);margin:0 auto;display:flex;align-items:center;justify-content:center}
.card .icon.red{background:var(--red)}
.card .icon svg{width:50px;height:50px}
.card h4{margin-top:18px;font-size:17px;font-weight:700;color:#222}
.card p{margin:14px auto 0;width:270px;font-size:13.5px;line-height:22px;color:#888}
.card .link{margin-top:16px;display:inline-flex;gap:6px;align-items:center;color:var(--red);font-weight:700;font-size:14px}

/* testimonials */
.testimonials{top:2947px;height:527px;background:linear-gradient(180deg,var(--red) 0%,#c50606 60%,#b90000 100%)}
.testimonials .shape{position:absolute;left:0;width:1200px}
.testimonials h2{position:absolute;left:320px;top:170px;font-family:'Michroma',sans-serif;font-weight:400;color:#fff;font-size:28px;letter-spacing:1px}
.avatar{position:absolute;left:182px;top:218px;width:100px;height:100px;transform:rotate(45deg);border:4px solid #fff;background:linear-gradient(135deg,#7fb4e2,#3d6f9f);box-shadow:0 4px 10px rgba(0,0,0,.3)}
.quote-text{position:absolute;left:321px;top:228px;width:680px;color:#fff;font-style:italic;font-size:15px;line-height:27px}
.quote-mark{position:absolute;font-family:Georgia,serif;font-size:60px;color:rgba(255,255,255,.35);line-height:1}
.person{position:absolute;left:321px;top:328px;color:#fff}
.person strong{display:block;font-size:17px;font-weight:500}
.person small{font-size:11.5px}
.arrow{position:absolute;top:258px;width:28px;height:40px}

/* contact */
.contact{top:3474px;height:666px}
.contact .title{margin-top:42px}
.info{position:absolute;top:150px;display:flex;gap:14px;align-items:flex-start}
.info svg{width:50px;height:50px;flex:none}
.info h5{font-size:15px;font-weight:700;color:#222;margin-top:2px}
.info p{font-size:13.5px;line-height:20px;color:#888;margin-top:4px}
.form{position:absolute;top:259px;left:123px;width:954px;height:250px}
.field{position:absolute;height:54px;border:1px solid #e0e0e0;background:#fafafa;font-size:12.5px;color:#777;padding:18px 0 0 20px;display:flex;gap:6px;align-items:flex-start}
.field svg{width:12px;height:12px;margin-top:1px}
.submit{position:absolute;left:532px;top:559px;width:134px;height:38px;font-size:15px}

/* footer */
.site-footer{top:4140px;height:461px;background:var(--grey-dark);color:#fff}
.site-footer .curve{position:absolute;left:0;top:0;width:1200px;height:120px}
.f-brand{position:absolute;left:107px;top:175px}
.f-brand .brand{color:#fff;font-size:32px}
.f-brand p{margin-top:22px;width:230px;font-size:12.5px;line-height:20px}
.f-social{display:flex;gap:10px;margin-top:22px}
.f-social span{width:28px;height:28px;border-radius:50%}
.f-col{position:absolute;top:164px}
.f-col h6{font-size:16px;font-weight:500;margin-bottom:18px}
.f-col li{list-style:none;font-size:13px;line-height:26px}
.f-contact li{display:flex;gap:10px;line-height:17px;margin-bottom:9px}
.f-contact li i{width:10px;height:10px;border-radius:50%;background:var(--red);margin-top:2px;flex:none}
.f-contact b{display:block;font-size:11px;font-weight:500}
.f-rule{position:absolute;left:111px;top:404px;width:978px;border-top:1px solid #5c5c5c}
.copyright{position:absolute;top:420px;width:100%;text-align:center;font-size:13.5px}
.to-top{position:absolute;left:1131px;top:338px;width:34px;height:34px;border-radius:50%;background:var(--red);display:flex;align-items:center;justify-content:center}
</style>
</head>
<body>

<header class="site-header">
  <div class="brand"><span class="dot"></span>Brightmara Sun</div>
  <div class="social-top"><span></span><span></span><span></span><span></span></div>
  <div class="call">
    <svg width="26" height="26" viewBox="0 0 24 24" fill="none" stroke="#d10a0a" stroke-width="1.8"><path d="M5 3h4l2 5-3 2a12 12 0 0 0 6 6l2-3 5 2v4a2 2 0 0 1-2 2A17 17 0 0 1 3 5a2 2 0 0 1 2-2z"/></svg>
    <div><small>Call Now</small><strong>(555) 014.2270</strong></div>
  </div>
  <div class="btn quote">Request A Quote</div>
  <nav class="nav"><span class="active">Home</span><span>About Us</span><span>Services</span><span>Projects</span><span>How It Works</span><span>Blog</span><span>FAQ</span><span>Contact Us</span>
    <svg width="15" height="15" viewBox="0 0 24 24" fill="none" stroke="#222" stroke-width="3"><circle cx="10" cy="10" r="7"/><path d="M15 15l6 6"/></svg></nav>
</header>

<section class="hero" role="img" aria-label="Aerial view of a car park covered with rows of solar panel canopies">
  <div class="hero-copy">
    <div class="brand"><span class="dot"></span>Brightmara Sun</div>
    <p>Sed ut perspiciatis unde omnis iste natus error sit voluptatem accusantium doloremque laudantium</p>
    <div class="btn">GET STARTED <svg viewBox="0 0 16 16"><circle cx="8" cy="8" r="8" fill="#fff"/><path d="M6.5 4.5 10 8l-3.5 3.5" stroke="#d10a0a" stroke-width="2" fill="none"/></svg></div>
  </div>
  <svg class="hero-curve" viewBox="0 0 1200 106" preserveAspectRatio="none">
    <path d="M110 60 Q600 -20 1090 60 Q600 10 110 60Z" fill="#d10a0a"/>
    <path d="M0 106 Q600 -30 1200 106Z" fill="#fff"/>
  </svg>
</section>

<section class="about">
  <h2 class="title">ABOUT <b>US</b></h2>
  <p>Lorem ipsum dolor sit amet, consectetur adipiscing elit, sed do eiusmod tempor incididunt ut labore et dolore magna aliqua. Ut enim ad minim veniam, quis nostrud exercitation ullamco laboris nisi ut aliquip ex ea commodo consequat. Duis aute irure dolor in reprehenderit in voluptate velit esse cillum dolore eu fugiat nulla pariatur.</p>
  <div class="features">
    <div class="feature red" style="left:96px"><div class="disc"><svg viewBox="0 0 24 24" fill="#fff"><path d="M12 2a7 7 0 0 0-7 7c0 5 7 13 7 13s7-8 7-13a7 7 0 0 0-7-7zm0 9.5A2.5 2.5 0 1 1 12 6.5a2.5 2.5 0 0 1 0 5z"/></svg>Australia's Largest Solar Company</div><span class="knot"></span></div>
    <div class="feature" style="left:351px"><div class="disc"><svg viewBox="0 0 24 24" fill="#fff"><circle cx="12" cy="12" r="3"/><circle cx="6" cy="13" r="2.2"/><circle cx="18" cy="13" r="2.2"/><path d="M7 22a5 5 0 0 1 10 0zM2 21a4 4 0 0 1 6-3l-1 3zM22 21a4 4 0 0 0-6-3l1 3z"/><path d="M6 3l.8 1.6 1.7.2-1.3 1.2.4 1.7L6 6.8l-1.6.9.4-1.7L3.5 4.8l1.7-.2zM12 2l.8 1.6 1.7.2-1.3 1.2.4 1.7L12 5.8l-1.6.9.4-1.7-1.3-1.2 1.7-.2zM18 3l.8 1.6 1.7.2-1.3 1.2.4 1.7L18 6.8l-1.6.9.4-1.7-1.3-1.2 1.7-.2z"/></svg>Only Solar Provider With 2854 + Five Star Reviews</div><span class="knot"></span></div>
    <div class="feature" style="left:607px"><div class="disc"><svg viewBox="0 0 24 24" fill="none" stroke="#fff" stroke-width="2"><path d="M12 2l8 3v6c0 5-3.5 9-8 11-4.5-2-8-6-8-11V5z"/><path d="M8 12l3 3 5-6"/></svg>Most Trusted Solar leases</div><span class="knot"></span></div>
    <div class="feature" style="left:862px"><div class="disc"><svg viewBox="0 0 24 24" fill="none" stroke="#fff" stroke-width="2"><path d="M3 21h18M6 21v-5h4v5M10 21v-9h4v9M14 21V8h4v13M19 6V2m0 0-2 2m2-2 2 2"/></svg>Over 20yrs combined solar experience</div></div>
  </div>
</section>

<section class="services">
  <h2 class="title"><b>OUR</b> SERVICES</h2>
  <div class="service-row">
    <div class="photo-house" role="img" aria-label="Blue house with solar panels on its roof"></div>
    <div class="panel grey"><span class="notch"></span><h3>Solar Ownership</h3><p>Lorem ipsum dolor sitconsectetur adipiscing elit, sed do eiusmod tempor incididunt ut labore et dolore magna aliqua. Ut enim ad minim veniam, quis nostrud exercitation ullamco laboris nisi ut aliquip ex ea commodo consequat.</p><div class="more">READ MORE <svg width="13" height="13" viewBox="0 0 16 16"><circle cx="8" cy="8" r="8" fill="#555"/><path d="M6.5 4.5 10 8l-3.5 3.5" stroke="#fff" stroke-width="2" fill="none"/></svg></div></div>
    <div class="photo-roof" role="img" aria-label="Tiled rooftop with solar panels overlooking hills"></div>
    <div class="panel red"><span class="notch"></span><h3>Leases Solar</h3><p>Lorem ipsum dolor sitconsectetur adipiscing elit, sed do eiusmod tempor incididunt ut labore et dolore magna aliqua. Ut enim ad minim veniam, quis nostrud exercitation ullamco laboris nisi ut aliquip ex ea commodo consequat.</p><div class="more">READ MORE <svg width="13" height="13" viewBox="0 0 16 16"><circle cx="8" cy="8" r="8" fill="#d10a0a"/><path d="M6.5 4.5 10 8l-3.5 3.5" stroke="#fff" stroke-width="2" fill="none"/></svg></div></div>
  </div>
</section>

<section class="how">
  <div class="photo" role="img" aria-label="Technician installing solar panels on a roof"></div>
  <div class="copy">
    <h2 class="title">HOW DOES <b>IT WORK?</b></h2>
    <p>Sed ut perspiciatis unde omnis iste natus error sit voluptatem accusantium doloremque laudantium, totam rem aperiam, eaque ipsa quae ab illo inventore veritatis et quasi architecto beatae vitae dicta sunt explicabo. Nemo enim ipsam voluptatem quia voluptas sit aspernatur aut odit aut fugit, sed quia consequuntur magni dolores eos qui ratione sequi nesciunt.</p>
    <div class="btn">LEARN MORE <svg viewBox="0 0 16 16"><circle cx="8" cy="8" r="8" fill="#fff"/><path d="M6.5 4.5 10 8l-3.5 3.5" stroke="#d10a0a" stroke-width="2" fill="none"/></svg></div>
  </div>
</section>

<section class="why">
  <h2 class="title"><b>WHY</b> CHOOSE US</h2>
  <div class="cards">
    <div class="card"><div class="icon"><svg viewBox="0 0 24 24" fill="none" stroke="#fff" stroke-width="1.6"><path d="M3 11l9-7 9 7M5 10v10h14V10M10 20v-6h4v6"/></svg></div><h4>LOCAL</h4><p>Lorem ipsum dolor sit amet, consectetur adipiscing elit, sed do eiusmod tempor incididunt ut labore et dolore</p><div class="link">READ MORE <svg width="13" height="13" viewBox="0 0 16 16"><circle cx="8" cy="8" r="8" fill="#d10a0a"/><path d="M6.5 4.5 10 8l-3.5 3.5" stroke="#fff" stroke-width="2" fill="none"/></svg></div></div>
    <div class="card"><div class="icon red"><svg viewBox="0 0 24 24" fill="none" stroke="#fff" stroke-width="1.6"><path d="M4 18l3-9h13l-3 9zM9.5 9l-2 9M14 9l-2 9M5.5 13.5h13M11 18v3M7 21h8M6 3v3M3 6h3M9 3.5l-1.5 1.5"/></svg></div><h4>RESPONSIBLE</h4><p>Lorem ipsum dolor sit amet, consectetur adipiscing elit, sed do eiusmod tempor incididunt ut labore et dolore</p><div class="link">READ MORE <svg width="13" height="13" viewBox="0 0 16 16"><circle cx="8" cy="8" r="8" fill="#d10a0a"/><path d="M6.5 4.5 10 8l-3.5 3.5" stroke="#fff" stroke-width="2" fill="none"/></svg></div></div>
    <div class="card"><div class="icon"><svg viewBox="0 0 24 24" fill="none" stroke="#fff" stroke-width="1.6"><rect x="4" y="3" width="16" height="12" rx="1"/><path d="M8 19h8M12 15v4M8 11l3-3 2 2 3-3"/></svg></div><h4>GREEN ENERGY</h4><p>Lorem ipsum dolor sit amet, consectetur adipiscing elit, sed do eiusmod tempor incididunt ut labore et dolore</p><div class="link">READ MORE <svg width="13" height="13" viewBox="0 0 16 16"><circle cx="8" cy="8" r="8" fill="#d10a0a"/><path d="M6.5 4.5 10 8l-3.5 3.5" stroke="#fff" stroke-width="2" fill="none"/></svg></div></div>
  </div>
</section>

<section class="testimonials">
  <svg class="shape" style="top:0;height:90px" viewBox="0 0 1200 90" preserveAspectRatio="none"><path d="M0 0H1200 Q600 150 0 0Z" fill="#d9dadc"/></svg>
  <svg class="shape" style="bottom:0;height:80px" viewBox="0 0 1200 80" preserveAspectRatio="none"><path d="M0 80 Q600 -50 1200 80Z" fill="#fff"/></svg>
  <h2>WHAT OUR CLIENTS HAVE TO SAY</h2>
  <svg class="arrow" style="left:106px" viewBox="0 0 28 40" fill="none" stroke="#fff" stroke-width="4"><path d="M22 4 6 20l16 16"/></svg>
  <svg class="arrow" style="left:1061px" viewBox="0 0 28 40" fill="none" stroke="#fff" stroke-width="4"><path d="M6 4l16 16L6 36"/></svg>
  <div class="avatar" role="img" aria-label="Client portrait"></div>
  <span class="quote-mark" style="left:276px;top:196px">“</span>
  <p class="quote-text">Lorem ipsum dolor sit amet, consectetur adipiscing elit, sed do eiusmod tempor incididunt ut labore et dolore magna aliqua. Ut enim ad minim veniam, quis nostrud exercitation ullamco laboris nisi ut aliquip ex ea commodo consequat.</p>
  <span class="quote-mark" style="left:592px;top:304px">”</span>
  <div class="person"><strong>Alex Morgan</strong><small>Company Name</small></div>
</section>

<section class="contact">
  <h2 class="title">CONTACT <b>US</b></h2>
  <div class="info" style="left:175px"><svg viewBox="0 0 48 48" fill="none" stroke="#d10a0a" stroke-width="2"><path d="M24 4a11 11 0 0 0-11 11c0 8 11 20 11 20s11-12 11-20A11 11 0 0 0 24 4z"/><circle cx="24" cy="15" r="4"/><path d="M14 32l-9 12h38l-9-12"/></svg><div><h5>LOCATION:</h5><p>4120 Harbor Lane, Suite 210,<br>Fairview, CA 90000</p></div></div>
  <div class="info" style="left:523px"><svg viewBox="0 0 48 48" fill="none" stroke="#d10a0a" stroke-width="2"><path d="M4 18l20-14 20 14v24H4z"/><path d="M4 18l20 14 20-14M4 42l15-13M44 42 29 29"/></svg><div><h5>EMAIL:</h5><p>info@brightmarasun.com</p></div></div>
  <div class="info" style="left:857px"><svg viewBox="0 0 48 48" fill="none" stroke="#d10a0a" stroke-width="2"><path d="M10 6h8l4 10-6 4a24 24 0 0 0 12 12l4-6 10 4v8a4 4 0 0 1-4 4C20 42 6 28 6 10a4 4 0 0 1 4-4z"/><path d="M28 6a14 14 0 0 1 14 14M28 12a8 8 0 0 1 8 8"/></svg><div><h5>PHONE:</h5><p>(555) 014-2270</p></div></div>
  <div class="form">
    <div class="field" style="left:0;top:0;width:470px"><svg viewBox="0 0 12 12" fill="#777"><circle cx="6" cy="3" r="2.5"/><path d="M1 12a5 5 0 0 1 10 0z"/></svg>First Name</div>
    <div class="field" style="left:484px;top:0;width:470px"><svg viewBox="0 0 12 12" fill="#777"><circle cx="6" cy="3" r="2.5"/><path d="M1 12a5 5 0 0 1 10 0z"/></svg>Last Name</div>
    <div class="field" style="left:0;top:66px;width:470px"><svg viewBox="0 0 12 12" fill="#777"><rect x="2" y="0" width="8" height="12"/></svg>Company</div>
    <div class="field" style="left:484px;top:66px;width:470px;height:184px"><svg viewBox="0 0 12 12" fill="#777"><path d="M1 2h10v6H5l-3 3V8H1z"/></svg>Message</div>
    <div class="field" style="left:0;top:131px;width:470px"><svg viewBox="0 0 12 12" fill="#777"><path d="M0 5l6-4 6 4v6H0z"/></svg>Email Address</div>
    <div class="field" style="left:0;top:196px;width:470px"><svg viewBox="0 0 12 12" fill="#777"><path d="M2 0h3l1 3-2 1a6 6 0 0 0 4 4l1-2 3 1v3a1 1 0 0 1-1 1A11 11 0 0 1 1 1a1 1 0 0 1 1-1z"/></svg>Phone Number</div>
  </div>
  <div class="btn submit">SUBMIT</div>
</section>

<footer class="site-footer">
  <svg class="curve" viewBox="0 0 1200 120" preserveAspectRatio="none">
    <path d="M110 22 Q600 170 1090 22 Q600 130 110 22Z" fill="#d10a0a"/>
    <path d="M0 0H1200 Q600 150 0 0Z" fill="#fff"/>
  </svg>
  <div class="f-brand">
    <div class="brand"><span class="dot"></span>Brightmara Sun</div>
    <p>Lorem ipsum dolor sit consectetur adipiscing elit, sed do eiusmod tempor incididunt ut labore</p>
    <div class="f-social"><span style="background:#1d4f9c"></span><span style="background:#1d9ce0"></span><span style="background:#d93a2b"></span><span style="background:#b0338a"></span></div>
  </div>
  <div class="f-col" style="left:409px"><h6>Quick Links</h6><ul><li>Home</li><li>About Us</li><li>Services</li><li>Projects</li><li>How It Works</li></ul></div>
  <div class="f-col" style="left:629px"><h6>About Company</h6><ul><li>Terms of Use</li><li>Terms &amp; Condition</li><li>News</li><li>Contact Us</li><li>FAQ</li></ul></div>
  <div class="f-col f-contact" style="left:870px"><h6>Contact Us</h6><ul>
    <li><i></i><span><b>Location</b>12 Willow Court Lakeview</span></li>
    <li><i></i><span><b>Phone</b>555 014 22700</span></li>
    <li><i></i><span><b>Fax</b>07 5550 1190</span></li>
    <li><i></i><span><b>Email</b>info@brightmarasun.com</span></li></ul></div>
  <div class="to-top"><svg width="14" height="14" viewBox="0 0 16 16" fill="none" stroke="#fff" stroke-width="2.5"><path d="M3 10l5-5 5 5"/></svg></div>
  <div class="f-rule"></div>
  <p class="copyright">2021 Copyright - brightmarasun &nbsp;| All Rights Reserved</p>
</footer>

</body>
</html>
```